Social Media Graphics - ALL TEXT RK

We are looking for a series of social media graphics for Instagram (standard size 1:1 (1080x1080px) that are ALL TEXT. We want the following quotes below on each graphic; one quote per graphic. AND, In very small letters at the bottom of each graphic, add @RKMarlowLive

The look and feel of these graphics should be complimentary to the color palette attached below; but keep them simple. But the design is up to you; at the end of this document, I provided various samples of all text graphics that I like as examples.

Target Market(s)

women looking to lose weight

Industry/Entity Type

health and wellness

Colors
E54698
E96AAD
F1A4CE
F9D9EA
FCEFF6

Requirements
Must have
• the quotes in the document
Should not have
• no stock photography

```html
<!DOCTYPE html>
<html lang="en">
<head>
<meta charset="utf-8">
<title>RK Marlow — All Text Quote Series</title>
<link rel="stylesheet" href="https://fonts.googleapis.com/css2?family=Bebas+Neue&family=Jost:wght@500;600&family=Outfit:wght@400;500&family=Allura&display=swap">
<style>
  :root {
    --pink-deep: #E54698;
    --pink-mid: #E96AAD;
    --pink-soft: #F1A4CE;
    --pink-pale: #F9D9EA;
    --pink-mist: #FCEFF6;
    --white: #ffffff;
  }
  * { margin: 0; padding: 0; box-sizing: border-box; }
  html, body { width: 1200px; height: 797px; overflow: hidden; background: var(--white); }
  .board { position: relative; width: 1200px; height: 797px; background: var(--white); }
  .tile { position: absolute; overflow: hidden; background: var(--pink-deep); }
  .row-top { top: 0; height: 392px; }
  .row-bottom { top: 401px; height: 396px; }
  .col-1 { left: 0; width: 394px; }
  .col-2 { left: 402px; width: 394px; }
  .col-3 { left: 804px; width: 396px; }
  .abs { position: absolute; }
  .bebas { font-family: "Bebas Neue", "Arial Narrow", sans-serif; font-weight: 400; }
  .quote-mark { font-family: "Bebas Neue", sans-serif; color: var(--pink-soft); font-size: 70px; line-height: 1; }
  .handle { font-family: "Outfit", sans-serif; font-size: 11px; color: var(--pink-pale); }

  /* Tile 1 */
  .sis-tag { left: 40px; top: 68px; width: 140px; height: 74px; background: var(--white); transform: rotate(-6deg);
             color: var(--pink-deep); font-size: 82px; line-height: 82px; text-align: center; padding-top: 2px; }
  .hormones { left: 114px; top: 178px; color: var(--white); font-size: 34px; line-height: 34px; }
  .weight { left: 114px; top: 258px; color: var(--white); font-size: 34px; line-height: 34px; }
  .handle-script { left: 117px; top: 340px; font-family: "Allura", cursive; font-size: 16px; color: var(--pink-soft); }

  /* Tile 2 */
  .natural { left: 0; width: 394px; top: 92px; text-align: center; font-family: "Jost", sans-serif; font-weight: 600;
             color: var(--pink-pale); font-size: 34px; line-height: 42px; letter-spacing: -0.3px; }
  .natural u { text-decoration-thickness: 2px; text-underline-offset: 5px; }
  .tile-2-handle { left: 0; width: 394px; top: 327px; text-align: center; }

  /* Tile 3 */
  .tile-3-mark { left: 0; width: 396px; top: 72px; text-align: center; }
  .overnight { left: 0; width: 396px; top: 137px; text-align: center; color: var(--pink-pale); font-size: 33px; line-height: 34px; }
  .tile-3-handle { left: 0; width: 396px; top: 329px; text-align: center; font-size: 16px; color: var(--pink-pale); letter-spacing: 0.5px; }

  /* Tile 4 */
  .col-1.row-bottom { background: linear-gradient(90deg, var(--pink-deep) 0 305px, var(--pink-mid) 305px, var(--pink-soft) 394px); }
  .one-night { left: 40px; top: 56px; color: var(--pink-pale); font-size: 46px; line-height: 44px; }
  .bloat { left: 40px; top: 258px; color: var(--pink-pale); font-size: 22px; line-height: 23px; }
  .tile-4-handle { left: 40px; top: 350px; }

  /* Tile 5 */
  .col-2.row-bottom { background: var(--pink-pale); }
  .torn-paper { left: 0; top: 0; width: 394px; height: 396px; }
  .tile-5-mark { left: 0; width: 394px; top: 50px; text-align: center; color: var(--pink-deep); font-size: 64px; }
  .stubborn { left: 36px; width: 260px; top: 110px; text-align: center; color: var(--pink-pale); font-size: 30px; line-height: 40px; transform: rotate(-2deg); }
  .stubborn u { text-decoration-thickness: 2px; text-underline-offset: 4px; }
  .tile-5-handle { left: 36px; width: 260px; top: 282px; text-align: center; font-size: 15px; color: var(--pink-pale); letter-spacing: 0.5px; }

  /* Tile 6 */
  .col-3.row-bottom { background: radial-gradient(circle at 90% 18%, var(--pink-soft) 0, var(--pink-mid) 35%, var(--pink-deep) 80%); }
  .tile-6-mark { left: 330px; top: 42px; color: var(--pink-pale); font-size: 58px; }
  .flatter { left: 38px; top: 96px; font-family: "Outfit", sans-serif; font-weight: 500; color: var(--white); font-size: 38px; line-height: 40px; }
  .magic-box { left: 38px; top: 226px; background: var(--white); padding: 5px 10px 6px 12px; border-left: 4px solid var(--pink-mid);
               font-family: "Outfit", sans-serif; font-weight: 500; color: var(--pink-deep); font-size: 18px; line-height: 21px; }
  .tile-6-handle { left: 38px; top: 350px; }
</style>
</head>
<body>
<main class="board">

  <section class="tile row-top col-1">
    <div class="abs quote-mark" style="left:36px;top:28px;">“</div>
    <div class="abs bebas sis-tag">SIS,</div>
    <p class="abs bebas hormones">YOUR HORMONES<br>ARE OUT OF WHACK</p>
    <p class="abs bebas weight">THAT'S WHY THE<br>WEIGHT WON'T BUDGE</p>
    <p class="abs handle-script">@RKMarlowLive</p>
  </section>

  <section class="tile row-top col-2">
    <p class="abs natural">Finally-a <u>Natural</u><br><u>Solution</u> That<br>Flattens Your<br>Belly And <u>Eases</u><br><u>Stomach Bloat</u>!</p>
    <p class="abs handle tile-2-handle">@RKMarlowLive</p>
  </section>

  <section class="tile row-top col-3">
    <div class="abs quote-mark tile-3-mark">“</div>
    <p class="abs bebas overnight">WAKE UP TOMORROW<br>WITH A FLATTER BELLY- YES,<br>THIS OVERNIGHT REMEDY<br>WORKS LIKE MAGIC!</p>
    <p class="abs bebas tile-3-handle">@RKMARLOWLIVE</p>
  </section>

  <section class="tile row-bottom col-1">
    <p class="abs bebas one-night">ONE SUPPLEMENT,<br>ONE NIGHT;</p>
    <p class="abs bebas bloat">YOUR BELLY BLOAT<br>COULD BE GONE BY MORNING.<br>HERE'S HOW IT WORKS!</p>
    <p class="abs handle tile-4-handle">@RKMarlowLive</p>
  </section>

  <section class="tile row-bottom col-2">
    <svg class="abs torn-paper" viewBox="0 0 394 396" aria-hidden="true">
      <defs>
        <filter id="paper-shadow" x="-10%" y="-10%" width="130%" height="130%">
          <feDropShadow dx="3" dy="6" stdDeviation="6" flood-color="#b0306f" flood-opacity="0.35"/>
        </filter>
      </defs>
      <g transform="rotate(-6 170 200)" filter="url(#paper-shadow)">
        <polygon fill="#ffffff" points="24,82 40,74 52,84 70,70 86,80 100,68 118,78 134,66 152,76 170,64 186,74 204,62 220,72 238,60 254,70 270,58 286,68 300,56 312,70 316,330 302,338 288,330 270,340 252,332 234,342 216,334 198,344 180,336 162,346 144,338 126,348 108,340 90,350 72,342 54,352 36,344 26,352"/>
        <polygon fill="#E54698" points="30,90 44,82 56,92 72,78 88,88 102,76 120,86 136,74 154,84 170,72 188,82 204,70 222,80 238,68 256,78 270,66 288,76 300,64 306,76 310,324 296,330 282,322 264,332 246,324 228,334 210,326 192,336 174,328 156,338 138,330 120,340 102,332 84,342 66,334 48,344 32,338"/>
      </g>
    </svg>
    <div class="abs quote-mark tile-5-mark">“</div>
    <p class="abs bebas stubborn"><u>THAT STUBBORN</u><br><u>BELLY FAT ISN'T YOUR</u><br><u>FAULT</u> - HERE'S WHAT<br>NO ONE TELLS YOU.</p>
    <p class="abs bebas tile-5-handle">@RKMARLOWLIVE</p>
  </section>

  <section class="tile row-bottom col-3">
    <div class="abs quote-mark tile-6-mark">“</div>
    <p class="abs flatter">Wake up<br>tomorrow with<br>a flatter belly!</p>
    <p class="abs magic-box">Yes, this overnight<br>remedy works like magic!</p>
    <p class="abs handle tile-6-handle">@RKMarlowLive</p>
  </section>

</main>
</body>
</html>
```